Korvane 24/7 Gym & Health Bar Webpage

We need a professional and interactive webpage for a 24/7 health club.
Our approach is professional yet friendly offering holitic professional services for both general and special populations, along with flexible 24/7 gym and group fitness memberships. Professional services that we offer;
Exercise Physiologist
Strength & Conditioning
Physiotherapy
Chiropractor
Nutrition
Personal Training
we also service acute and chronic injuries, work cover, and veteran affairs

We also have a well-being bar offers healthy food, beverages and wide range of supplements.
We send out regular newsletters and want it to be interactive with social media and e-commerce.
Final design should demonstrate a holistic approach where clients have access to a wide range of health services within a professional health club environment. needs to be phone and table friendly please

i have attached a template i had been working on but wasn't happy with it

Target Market(s)

wide demographic including:

Special population - older demographic looking for professional services. Doctors will be referring clients to us also

24/7 gym - aged 25+ yrs, male and female

Industry/Entity Type

Health And Wellness

Coding

Coded - Design and coding required

Number of Pages Required

5+ page

Colors
33a6d7
add136
ffffff
0355a3

Requirements
Must have
• atmosphere and professionalism whilst inviting and sincere
• social media interaction & blog page
• clear navigation
• mobile and table friendly
• Brisk E-newsletter sign up
• testimonials
Nice to have
• customer feedback option
• FAQ
• opportunity to integrate online shop
• ability to download free visit pass

```html
<!DOCTYPE html>
<html lang="en">
<head>
<meta charset="utf-8">
<title>Korvane Health &amp; Fitness</title>
<link href="https://fonts.googleapis.com/css2?family=Raleway:wght@300;400;500;600;700;800&display=swap" rel="stylesheet">
<style>
:root{
  --blue:#0355a3;
  --blue-mid:#1572c9;
  --sky:#33a6d7;
  --lime:#add136;
  --white:#ffffff;
  --ink:#444a52;
  --muted:#6d7177;
  --panel:#f2f3f5;
  --dark:#2b2d30;
  --footer:#1b1c1e;
  --line:#d5d8dc;
}
*{margin:0;padding:0;box-sizing:border-box}
html,body{width:1200px;height:4167px;overflow:hidden}
body{font-family:'Raleway',sans-serif;color:var(--ink);background:var(--white);position:relative}
.page{position:relative;width:1200px;height:4167px;overflow:hidden}

/* header */
.site-header{position:absolute;left:0;top:0;width:1200px;height:153px;background:var(--white)}
.brand{position:absolute;left:95px;top:26px;display:flex;align-items:center;gap:14px}
.brand-dot{width:58px;height:58px;border-radius:50%;background:var(--blue)}
.brand-name{font-size:46px;font-weight:700;color:var(--blue);letter-spacing:1px;line-height:1}
.brand-tag{position:absolute;left:125px;top:106px;font-size:13px;font-weight:600;color:var(--blue)}
.main-nav{position:absolute;left:555px;top:66px;display:flex;align-items:center;gap:30px}
.main-nav a{font-size:21px;font-weight:700;color:var(--blue);text-decoration:none}
.main-nav a.active{background:var(--blue);color:var(--white);padding:8px 16px;border-radius:3px}

/* hero */
.hero{position:absolute;left:0;top:153px;width:1200px;height:417px;background:linear-gradient(90deg,#0d63bd 0%,#1b82d6 55%,#0f66c0 100%)}
.hero-photo{position:absolute;left:0;top:0;width:670px;height:417px;background:linear-gradient(90deg,#5d8fc4 0%,#8fb8de 50%,rgba(27,130,214,0) 100%)}
.hero-copy{position:absolute;left:688px;top:60px;width:380px;color:var(--white)}
.hero-copy h1{font-size:54px;font-weight:400;line-height:1.1}
.hero-copy h2{font-size:28px;font-weight:400;margin-top:22px}
.hero-copy p{font-size:18px;line-height:1.45;margin-top:14px;font-weight:400}
.btn-lime{display:inline-block;background:var(--lime);color:#1c2a08;font-weight:700;font-size:18px;padding:11px 22px;border-radius:4px;margin-top:20px}
.hero-arrow{position:absolute;top:170px}

/* welcome */
.welcome{position:absolute;left:0;top:570px;width:1200px;height:300px;text-align:center}
.welcome h2{margin-top:40px;font-size:40px;font-weight:400;color:var(--sky)}
.welcome p{width:900px;margin:40px auto 0;font-size:19px;line-height:1.6;color:var(--ink)}

/* shared blue band */
.band{position:absolute;left:0;width:1200px;background:linear-gradient(90deg,#0a57a8 0%,#1a7fd4 50%,#0a57a8 100%)}
.band-title{position:absolute;width:560px;left:130px;text-align:center;color:var(--white)}
.band-title h2{font-size:62px;font-weight:300;line-height:1}
.band-title p{font-size:19px;line-height:1.55;margin-top:28px}
.band-photo{position:absolute;background:linear-gradient(135deg,#a9b7c6,#5d7590)}

.panel{position:absolute;left:105px;width:990px;background:linear-gradient(180deg,#ffffff 0%,#eeeff1 100%);border-radius:24px 24px 0 0}

/* services */
.service-grid{position:absolute;left:0;top:20px;width:990px;display:grid;grid-template-columns:repeat(3,1fr);row-gap:40px}
.service{text-align:center}
.service-pic{width:140px;height:140px;border-radius:50%;margin:0 auto;border:4px solid var(--white);box-shadow:0 0 0 2px var(--sky);background:linear-gradient(135deg,#d9e4ef,#8aa6c2)}
.service h3{font-size:19px;font-weight:700;color:var(--blue);margin-top:18px}
.service p{font-size:15px;line-height:1.5;color:var(--muted);width:280px;margin:8px auto 0}
.learn{display:inline-block;font-size:16px;font-weight:700;color:var(--blue);margin-top:14px}

/* testimonial */
.testimonial{position:absolute;left:0;top:1717px;width:1200px;height:469px;background:linear-gradient(180deg,#4a4c50 0%,#2e3033 100%)}
.testimonial .inner{position:absolute;left:0;top:0;width:1200px;text-align:center;color:var(--white)}
.testimonial h2{font-size:36px;font-weight:600;margin-top:30px}
.quote-mark{margin-top:22px}
.testimonial blockquote{width:760px;margin:22px auto 0;font-size:20px;font-weight:600;line-height:1.6}
.client{margin-top:16px;font-size:26px;font-weight:700;display:flex;justify-content:center;align-items:center;gap:14px}
.client span{font-size:18px;font-weight:600;display:flex;align-items:center;gap:6px}
.avatar{width:112px;height:112px;border-radius:50%;margin:28px auto 0;border:4px solid var(--white);background:linear-gradient(135deg,#c9b7a8,#7d6a5d)}
.side-arrow{position:absolute;width:32px;height:32px;border-radius:50%;background:var(--white);display:flex;align-items:center;justify-content:center}

/* blog */
.blog-grid{position:absolute;left:20px;top:56px;width:950px;display:grid;grid-template-columns:repeat(3,292px);column-gap:36px}
.post-pic{position:relative;height:205px;background:linear-gradient(135deg,#c4d6e6,#7f9bb6)}
.post-date{position:absolute;left:0;bottom:0;width:100%;height:28px;background:rgba(3,85,163,.85);color:var(--white);font-size:12px;font-weight:600;padding:7px 10px}
.post h3{font-size:17px;font-weight:700;color:var(--blue);margin-top:16px}
.post p{font-size:15px;line-height:1.5;color:var(--muted);margin-top:6px}

/* shop */
.shop{position:absolute;left:0;top:2828px;width:1200px;height:417px;background:linear-gradient(180deg,#3c3e42 0%,#26282b 100%)}
.shop h2{position:absolute;top:28px;width:1200px;text-align:center;color:var(--white);font-size:38px;font-weight:600}
.shop-grid{position:absolute;left:125px;top:117px;display:grid;grid-template-columns:repeat(3,292px);column-gap:36px}
.product{height:250px;background:var(--white);position:relative}
.product-pic{position:absolute;left:20px;top:20px;right:20px;height:168px}
.product-bar{position:absolute;left:0;bottom:0;width:100%;height:42px;background:var(--blue);color:var(--white);display:flex;align-items:center;justify-content:space-between;padding:0 10px;font-size:18px;font-weight:700}
.cart{width:28px;height:28px;border-radius:50%;background:var(--white);display:flex;align-items:center;justify-content:center}

/* faq + feedback */
.section-h{font-size:40px;font-weight:400;color:var(--blue)}
.faq{position:absolute;left:78px;top:3276px;width:472px}
.faq-list{margin-top:20px;border:1px solid var(--line)}
.faq-item{border-bottom:1px solid var(--line);padding:10px 12px;display:flex;gap:12px;font-size:16px;font-weight:600;color:var(--blue)}
.faq-item:last-child{border-bottom:none}
.faq-item .sign{font-size:20px;line-height:18px;color:#333;width:14px}
.faq-answer{font-size:14px;font-weight:500;color:var(--muted);line-height:1.55;margin-top:10px}
.divider{position:absolute;left:600px;top:3290px;width:1px;height:350px;background:var(--line)}
.feedback{position:absolute;left:645px;top:3276px;width:470px}
.field{border:1px solid #c9cdd2;background:var(--white);font-size:13px;color:#9a9ea3;padding:10px 12px;margin-top:20px}
.field.area{height:126px;margin-top:25px}
.btn-blue{display:inline-block;background:var(--blue);color:var(--white);font-weight:700;font-size:17px;padding:12px 32px;margin-top:30px;border-radius:2px}

/* subscribe */
.subscribe{position:absolute;left:0;top:3703px;width:1200px;height:208px;background:linear-gradient(90deg,#0a57a8,#1a7fd4 50%,#0a57a8);text-align:center;color:var(--white)}
.subscribe h2{font-size:40px;font-weight:400;margin-top:30px}
.subscribe p{font-size:14px;margin-top:10px}
.sub-row{position:absolute;left:153px;top:125px;display:flex;gap:64px}
.sub-field{width:311px;height:37px;background:var(--white);color:#9a9ea3;font-size:13px;text-align:left;padding:11px 12px}
.sub-btn{width:144px;height:37px;background:var(--lime);color:#1c2a08;font-weight:700;font-size:20px;padding-top:6px}

/* footer */
.site-footer{position:absolute;left:0;top:3911px;width:1200px;height:256px;background:var(--footer);color:#d9dadc}
.foot-nav{position:absolute;left:78px;top:30px;display:flex;align-items:center;gap:40px;font-size:17px;font-weight:500}
.foot-nav .active{border:2px solid var(--blue);border-radius:20px;padding:8px 22px;color:var(--lime)}
.socials{position:absolute;left:833px;top:28px;display:flex;gap:30px}
.socials span{width:46px;height:46px;border-radius:2px;display:block}
.foot-line{position:absolute;left:78px;top:103px;width:1044px;height:1px;background:#3a3c40}
.foot-contact h3{position:absolute;left:130px;top:125px;font-size:24px;font-weight:500;color:var(--white)}
.contact-row{position:absolute;left:78px;top:158px;display:flex;align-items:flex-start;gap:22px;font-size:14px}
.ci{width:40px;height:40px;border-radius:50%;display:flex;align-items:center;justify-content:center;flex-shrink:0}
.copy{position:absolute;right:78px;top:173px;font-size:13px}
.copy b{color:var(--lime);font-weight:600}
</style>
</head>
<body>
<div class="page">

  <header class="site-header">
    <div class="brand"><span class="brand-dot"></span><span class="brand-name">Korvane</span></div>
    <div class="brand-tag">Move well. Recover fast. Stay strong</div>
    <nav class="main-nav">
      <a class="active" href="#">Home</a>
      <a href="#">About</a>
      <a href="#">Service</a>
      <a href="#">Blog</a>
      <a href="#">Shop</a>
      <a href="#">Contact Us</a>
    </nav>
  </header>

  <section class="hero">
    <div class="hero-photo" role="img" aria-label="Physiotherapist helping a client on crutches"></div>
    <svg class="hero-arrow" style="left:28px" width="26" height="60" viewBox="0 0 26 60"><path d="M22 4 L5 30 L22 56" fill="none" stroke="#fff" stroke-width="3"/></svg>
    <svg class="hero-arrow" style="right:28px" width="26" height="60" viewBox="0 0 26 60"><path d="M4 4 L21 30 L4 56" fill="none" stroke="#fff" stroke-width="3"/></svg>
    <div class="hero-copy">
      <h1>Quick Recover</h1>
      <h2>With our Help</h2>
      <p>Lorem Ipsum is simply dummy text of the printing and typesetting industry. Lorem Ipsum has been the industry'</p>
      <span class="btn-lime">READ MORE</span>
    </div>
  </section>

  <section class="welcome">
    <h2>Welcome To Korvane Health &amp; Fitness</h2>
    <p>Lorem Ipsum is simply dummy text of the printing and typesetting industry. Lorem Ipsum has been the industry's standard dummy text ever since the 1500s. when an unknown printer took a galley of type and scrambled it to make a type specimen book. It has survived not only five centuries.</p>
  </section>

  <section class="services">
    <div class="band" style="top:870px;height:240px"></div>
    <div class="band-title" style="top:895px">
      <h2>Service</h2>
      <p>Lorem Ipsum is simply dummy text of the printing and<br>typesetting industry. Lorem Ipsum has been.</p>
    </div>
    <div class="band-photo" style="left:720px;top:862px;width:230px;height:210px;background:linear-gradient(135deg,#b9c6d3,#56708c)" role="img" aria-label="Trainer and client lifting dumbbells"></div>
    <div class="panel" style="top:1070px;height:630px">
      <div class="service-grid">
        <div class="service"><div class="service-pic" role="img" aria-label="Exercise physiologist with client"></div><h3>Exercise Physiologist</h3><p>Lorem Ipsum is simply dummy text of the pri and typesetting industry.</p><span class="learn">Learn More &#187;</span></div>
        <div class="service"><div class="service-pic" role="img" aria-label="Athlete strength training"></div><h3>Strength &amp; Conditioning</h3><p>Lorem Ipsum is simply dummy text of the pri and typesetting industry.</p><span class="learn">Learn More &#187;</span></div>
        <div class="service"><div class="service-pic" role="img" aria-label="Physiotherapy knee treatment"></div><h3>Physiotherapy</h3><p>Lorem Ipsum is simply dummy text of the pri and typesetting industry.</p><span class="learn">Learn More &#187;</span></div>
        <div class="service"><div class="service-pic" role="img" aria-label="Therapist treating a client's neck"></div><h3>Exercise Physiologist</h3><p>Lorem Ipsum is simply dummy text of the pri and typesetting industry.</p><span class="learn">Learn More &#187;</span></div>
        <div class="service"><div class="service-pic" role="img" aria-label="Sports team conditioning session"></div><h3>Strength &amp; Conditioning</h3><p>Lorem Ipsum is simply dummy text of the pri and typesetting industry.</p><span class="learn">Learn More &#187;</span></div>
        <div class="service"><div class="service-pic" role="img" aria-label="Physiotherapist assisting a client"></div><h3>Physiotherapy</h3><p>Lorem Ipsum is simply dummy text of the pri and typesetting industry.</p><span class="learn">Learn More &#187;</span></div>
      </div>
    </div>
  </section>

  <section class="testimonial" role="img" aria-label="Group fitness class in a gym, darkened">
    <div class="inner">
      <h2>Our Client Say</h2>
      <svg class="quote-mark" width="52" height="40" viewBox="0 0 52 40"><path d="M2 38V22C2 10 8 3 20 1l2 5c-7 2-10 6-10 12h9v20zM30 38V22c0-12 6-19 18-21l2 5c-7 2-10 6-10 12h9v20z" fill="#9c9ea2"/></svg>
      <blockquote>Never believed I'll have such professional treatment. Great hospital. I will recommend this physiotherapy service to all my clients and friends.</blockquote>
      <div class="client">Marla Quinn <span><svg width="14" height="20" viewBox="0 0 14 20"><path d="M7 0a7 7 0 0 0-7 7c0 5 7 13 7 13s7-8 7-13a7 7 0 0 0-7-7zm0 10a3 3 0 1 1 0-6 3 3 0 0 1 0 6z" fill="#fff"/></svg>Lindale, OH</span></div>
      <div class="avatar" role="img" aria-label="Client portrait"></div>
    </div>
    <div class="side-arrow" style="left:58px;top:217px"><svg width="16" height="12" viewBox="0 0 16 12"><path d="M7 1 2 6l5 5M14 1 9 6l5 5" fill="none" stroke="#333" stroke-width="2"/></svg></div>
    <div class="side-arrow" style="right:58px;top:217px"><svg width="16" height="12" viewBox="0 0 16 12"><path d="M2 1l5 5-5 5M9 1l5 5-5 5" fill="none" stroke="#333" stroke-width="2"/></svg></div>
  </section>

  <section class="blog">
    <div class="band" style="top:2208px;height:306px"></div>
    <div class="band-title" style="top:2240px">
      <h2>Blog</h2>
      <p>Lorem Ipsum is simply dummy text of the printing and<br>typesetting industry. Lorem Ipsum has been.</p>
    </div>
    <div class="band-photo" style="left:736px;top:2205px;width:330px;height:250px;transform:rotate(-4deg);background:linear-gradient(135deg,#c7b5c9,#6a5b7a)" role="img" aria-label="Stack of fitness class photographs"></div>
    <div class="panel" style="top:2411px;height:381px">
      <div class="blog-grid">
        <article class="post"><div class="post-pic" role="img" aria-label="Woman stretching on a mat"><div class="post-date">20 March, 2015 / 17 Views</div></div><h3>The blog title</h3><p>Choro pertinacia eu eam. Per facer eligendi in. Erat principes dissentiet ex vim.</p></article>
        <article class="post"><div class="post-pic" role="img" aria-label="Smiling group in a fitness class"><div class="post-date">20 March, 2015 / 17 Views</div></div><h3>The blog title</h3><p>Choro pertinacia eu eam. Per facer eligendi in. Erat principes dissentiet ex vim.</p></article>
        <article class="post"><div class="post-pic" role="img" aria-label="Athlete drinking water after training"><div class="post-date">20 March, 2015 / 17 Views</div></div><h3>The blog title</h3><p>Choro pertinacia eu eam. Per facer eligendi in. Erat principes dissentiet ex vim.</p></article>
      </div>
    </div>
  </section>

  <section class="shop" role="img" aria-label="Gym floor background, darkened">
    <h2>Online Shop</h2>
    <div class="side-arrow" style="left:58px;top:214px"><svg width="16" height="12" viewBox="0 0 16 12"><path d="M7 1 2 6l5 5M14 1 9 6l5 5" fill="none" stroke="#333" stroke-width="2"/></svg></div>
    <div class="side-arrow" style="right:58px;top:214px"><svg width="16" height="12" viewBox="0 0 16 12"><path d="M2 1l5 5-5 5M9 1l5 5-5 5" fill="none" stroke="#333" stroke-width="2"/></svg></div>
    <div class="shop-grid">
      <div class="product"><div class="product-pic" role="img" aria-label="Woman using a stretch band" style="background:linear-gradient(180deg,#f4f4f4,#d8e6ee)"></div><div class="product-bar">Stretch Bands<span class="cart"><svg width="16" height="14" viewBox="0 0 16 14"><path d="M0 1h3l2 8h8l2-6H4" fill="none" stroke="#0355a3" stroke-width="1.8"/><circle cx="6" cy="12" r="1.3" fill="#0355a3"/><circle cx="12" cy="12" r="1.3" fill="#0355a3"/></svg></span></div></div>
      <div class="product"><div class="product-pic" role="img" aria-label="Blue foam roller" style="background:linear-gradient(135deg,#f4f6f9,#9fbbe2)"></div><div class="product-bar">Foam Roller Large<span class="cart"><svg width="16" height="14" viewBox="0 0 16 14"><path d="M0 1h3l2 8h8l2-6H4" fill="none" stroke="#0355a3" stroke-width="1.8"/><circle cx="6" cy="12" r="1.3" fill="#0355a3"/><circle cx="12" cy="12" r="1.3" fill="#0355a3"/></svg></span></div></div>
      <div class="product"><div class="product-pic" role="img" aria-label="Gift voucher card with a blue ribbon" style="background:linear-gradient(135deg,#6f7a84,#2f6fb0)"></div><div class="product-bar">Member Gift Voucher<span class="cart"><svg width="16" height="14" viewBox="0 0 16 14"><path d="M0 1h3l2 8h8l2-6H4" fill="none" stroke="#0355a3" stroke-width="1.8"/><circle cx="6" cy="12" r="1.3" fill="#0355a3"/><circle cx="12" cy="12" r="1.3" fill="#0355a3"/></svg></span></div></div>
    </div>
  </section>

  <section class="faq">
    <h2 class="section-h">FAQ</h2>
    <div class="faq-list">
      <div class="faq-item"><span class="sign">&#8211;</span><div>Lorem Ipsum is simply dummy text of the print.<div class="faq-answer">Lorem Ipsum is simply dummy text of the printing and typesetting industry. Lorem Ipsum has been the industry's standard dummy text ever since the 1500.</div></div></div>
      <div class="faq-item"><span class="sign">+</span><div>Lorem Ipsum is simply dummy text of the print.</div></div>
      <div class="faq-item"><span class="sign">+</span><div>Lorem Ipsum is simply dummy text of the print.</div></div>
      <div class="faq-item"><span class="sign">+</span><div>Lorem Ipsum is simply dummy text of the print.</div></div>
      <div class="faq-item"><span class="sign">+</span><div>Lorem Ipsum is simply dummy text of the print.</div></div>
    </div>
  </section>
  <div class="divider"></div>
  <section class="feedback">
    <h2 class="section-h">Customer Feedback</h2>
    <div class="field">Enter your Name</div>
    <div class="field area">Feedback</div>
    <span class="btn-blue">SUBMIT</span>
  </section>

  <section class="subscribe">
    <h2>Subscribe to Korvane Health &amp; Fitness</h2>
    <p>Lorem Ipsum is simply dummy text of the printing and typesetting industry. Lorem Ipsum has been the industry's standard.</p>
    <div class="sub-row">
      <div class="sub-field">Enter your Name</div>
      <div class="sub-field">Enter your Email</div>
      <div class="sub-btn">Subscribe</div>
    </div>
  </section>

  <footer class="site-footer">
    <nav class="foot-nav">
      <span class="active">Home</span><span>About</span><span>Terms &amp; Condition</span><span>Privacy Policy</span><span>Contact</span>
    </nav>
    <div class="socials" aria-label="Social media links">
      <span style="background:#3b5b9a"></span><span style="background:#2ea3df"></span><span style="background:#1a78b4"></span><span style="background:#c8232c"></span>
    </div>
    <div class="foot-line"></div>
    <div class="foot-contact">
      <h3>Contact Us</h3>
      <div class="contact-row">
        <span class="ci" style="background:var(--blue)"><svg width="20" height="18" viewBox="0 0 20 18"><path d="M10 1 1 9h3v8h5v-5h2v5h5V9h3z" fill="#fff"/></svg></span>
        <span style="width:200px;line-height:1.45;margin-top:2px">Lorem Ipsum is simply dummy text of the printing and typesetting industry.</span>
        <span class="ci" style="background:var(--lime);margin-left:18px"><svg width="14" height="20" viewBox="0 0 14 20"><rect x="1" y="1" width="12" height="18" rx="2" fill="none" stroke="#1c2a08" stroke-width="2"/><circle cx="7" cy="15.5" r="1.3" fill="#1c2a08"/></svg></span>
        <span style="margin-top:12px">Call : 555 014 229</span>
        <span class="ci" style="background:var(--lime);margin-left:18px"><svg width="20" height="18" viewBox="0 0 20 18"><rect x="5" y="1" width="10" height="5" fill="none" stroke="#1c2a08" stroke-width="2"/><rect x="1" y="6" width="18" height="8" rx="1" fill="#1c2a08"/><rect x="5" y="11" width="10" height="6" fill="#add136" stroke="#1c2a08" stroke-width="2"/></svg></span>
        <span style="margin-top:12px">Fax : 555 014 229</span>
      </div>
      <div class="copy">&#169; <b>Korvane Health &amp; Fitness</b> - 2015. All Rights Reserved.</div>
    </div>
  </footer>

</div>
</body>
</html>
```